Improve the UI for two Mobile Apps

Brevano licenses ERP software to mid-sized companies (50M plus). Brevano's product suite includes procurement, accounting and CRM applications.

We have two mobile Apps that integrate with our ERP applications - Tallyway Hub and Morrow Field Kit. The Tallyway Hub App allows a user to review and approve requisitions, purchase orders, supplier invoices and expense reports which are forwarded to the App from our ERP applications. The expense report App allows a user to enter travel expenses and attach photos of receipts.

We are satisfied with the functionality of both mobile Apps. Our goal is to improve the aesthetics (fonts, colors, graphics). We are looking for a clean, light weight, modern design. The design should also be consistent with our current Brevano colors (blue and green) and branding (see www.brevanosystems.com).

Documentation showing current screen shots for each App is attached (2 files).
Updates

Please focus on the 14 major forms in the attachment. The larger document includes about 40 forms. It is intended to illustrate the use of the Apps which hopefully is useful when considering design alternatives. We realize the budget may be insufficient for the complete redesign of both Apps. When accepting the final design we will negotiate a price for revising / completing all forms. At this point we will increase the project's budget or complete the remaining work in-house. Thanks, Derek...

Target Market(s)

We sell to mid-large sized corporations. Are primary customer is the purchasing agent.

Industry/Entity Type

Accounting

Number of Pages Required

5+ page

Requirements
Must have
• Clean, modern design of the major entry forms shown in the attached documents. I need graphics and colors only. Our developers will adjust the Apps. I have attached 2 sets of documents. The first 2 files illustrate the use of all forms in both apps. Several forms appear multiple times. The second set of 3 files include the unique forms in both apps (14 in total). These files are labeled "(major forms)".

```html
<!DOCTYPE html>
<html lang="en">
<head>
<meta charset="utf-8">
<title>Brevano – Tallyway Hub</title>
<link rel="stylesheet" href="https://fonts.googleapis.com/css2?family=Open+Sans:wght@400;600;700;800&display=swap">
<style>
  :root {
    --page-bg: #f3f3f3;
    --white: #ffffff;
    --ink: #111111;
    --brand-blue: #0b559f;
    --muted-teal: #2f7a90;
    --muted-teal-text: #9cc3cf;
    --field-green: #9fd27e;
    --icon-green: #7fbf5a;
    --submit-bg: #cfe8c0;
    --divider: rgba(255, 255, 255, 0.45);
  }
  * { box-sizing: border-box; margin: 0; padding: 0; }
  html, body {
    width: 1200px; height: 751px; overflow: hidden;
    background: var(--page-bg);
    font-family: "Open Sans", Arial, sans-serif;
  }
  .stage { position: relative; width: 1200px; height: 751px; }
  .app-screen {
    position: absolute; left: 400px; top: 20px;
    width: 320px; height: 568px;
    transform: scale(1.25); transform-origin: top left;
    background: var(--field-green);
    overflow: hidden;
    box-shadow: 0 2px 10px rgba(0,0,0,0.12);
  }
  .status-bar {
    position: absolute; left: 0; top: 0; width: 320px; height: 20px;
    background: var(--white); color: var(--ink);
    font-size: 12px; display: flex; align-items: center; padding: 0 6px;
  }
  .status-bar .carrier { display: flex; align-items: center; gap: 5px; }
  .status-bar .signal { letter-spacing: -1px; font-size: 9px; }
  .status-bar .battery-group { margin-left: auto; display: flex; align-items: center; gap: 4px; }
  .battery { width: 24px; height: 10px; border: 1px solid var(--ink); border-radius: 2px; padding: 1px; }
  .battery span { display: block; width: 82%; height: 100%; background: var(--ink); }
  .app-header {
    position: absolute; left: 0; top: 20px; width: 320px; height: 66px;
    background: var(--white);
    border-bottom: 2px solid #d4d4d4;
    display: flex; align-items: center; justify-content: center; gap: 6px;
  }
  .brand-name {
    font-weight: 800; font-size: 28px; letter-spacing: 0.5px;
    color: var(--brand-blue);
  }
  .brand-dot { width: 12px; height: 12px; border-radius: 50%; background: var(--icon-green); }
  .toolbar { position: absolute; top: 103px; right: 25px; display: flex; gap: 10px; }
  .tool-button {
    width: 35px; height: 35px; border-radius: 6px; background: var(--white);
    box-shadow: 1px 2px 2px rgba(0,0,0,0.25);
    display: flex; align-items: center; justify-content: center;
  }
  .screen-title {
    position: absolute; left: 10px; top: 153px; width: 297px; height: 42px;
    background: var(--brand-blue); color: var(--white);
    display: flex; align-items: center; gap: 10px; padding-left: 10px;
    font-weight: 700; font-size: 20px;
    box-shadow: 1px 2px 3px rgba(0,0,0,0.25);
  }
  .stat-row {
    position: absolute; left: 0; width: 320px; height: 58px;
    border-bottom: 1px solid var(--divider);
  }
  .stat-row.unprocessed { top: 213px; }
  .stat-row.actions { top: 270px; }
  .stat-label, .stat-value {
    position: absolute; top: 10px; height: 42px;
    display: flex; align-items: center;
    box-shadow: 1px 2px 3px rgba(0,0,0,0.2);
  }
  .stat-label { left: 48px; width: 175px; padding-left: 9px; font-size: 12px; }
  .stat-value { left: 243px; width: 64px; justify-content: center; font-size: 22px; }
  .unprocessed .stat-label, .unprocessed .stat-value { background: var(--brand-blue); color: var(--white); }
  .actions .stat-label, .actions .stat-value { background: var(--muted-teal); color: var(--muted-teal-text); }
  .submit-button {
    position: absolute; left: 10px; top: 444px; width: 297px; height: 41px;
    background: var(--submit-bg); color: var(--field-green);
    display: flex; align-items: center; justify-content: center;
    font-weight: 700; font-size: 20px;
    box-shadow: 1px 2px 3px rgba(0,0,0,0.15);
  }
  .help-link {
    position: absolute; left: 33px; top: 532px; width: 255px;
    display: flex; align-items: center; gap: 18px;
    color: var(--white); font-size: 13px;
  }
  .help-link::before, .help-link::after { content: ""; flex: 1; height: 1px; background: var(--white); }
</style>
</head>
<body>
<div class="stage">
  <div class="app-screen">
    <div class="status-bar">
      <div class="carrier"><span class="signal">●●●●</span><span>NIMBO</span>
        <svg width="14" height="10" viewBox="0 0 14 10"><path d="M1 3.5a9 9 0 0 1 12 0M3.2 5.6a6 6 0 0 1 7.6 0M5.3 7.7a3 3 0 0 1 3.4 0" fill="none" stroke="#111" stroke-width="1.5"/><circle cx="7" cy="9.2" r="0.8" fill="#111"/></svg>
      </div>
      <div class="battery-group"><span>82%</span><div class="battery"><span></span></div></div>
    </div>

    <header class="app-header">
      <span class="brand-name">BREVANO</span><span class="brand-dot"></span>
    </header>

    <nav class="toolbar">
      <div class="tool-button" aria-label="Back">
        <svg width="20" height="22" viewBox="0 0 20 22"><path d="M14 2 L5 11 L14 20" fill="none" stroke="var(--icon-green)" stroke-width="4" stroke-linecap="round" stroke-linejoin="round"/></svg>
      </div>
      <div class="tool-button" aria-label="Search">
        <svg width="26" height="26" viewBox="0 0 26 26"><circle cx="16" cy="10" r="7" fill="none" stroke="var(--icon-green)" stroke-width="3"/><path d="M11 15 L3 23" stroke="var(--icon-green)" stroke-width="4" stroke-linecap="round"/></svg>
      </div>
      <div class="tool-button" aria-label="Menu">
        <svg width="28" height="24" viewBox="0 0 28 24"><rect x="1" y="2" width="26" height="5" fill="var(--icon-green)"/><rect x="1" y="9.5" width="26" height="5" fill="var(--icon-green)"/><rect x="1" y="17" width="26" height="5" fill="var(--icon-green)"/></svg>
      </div>
    </nav>

    <h1 class="screen-title">
      <svg width="22" height="28" viewBox="0 0 22 28"><path d="M2 16 L8 25 L20 2" fill="none" stroke="#fff" stroke-width="4" stroke-linejoin="round"/></svg>
      TALLYWAY HUB
    </h1>

    <div class="stat-row unprocessed">
      <div class="stat-label">UNPROCESSED&nbsp; DOCS</div>
      <div class="stat-value">12</div>
    </div>
    <div class="stat-row actions">
      <div class="stat-label">YOUR ACTIONS</div>
      <div class="stat-value">0</div>
    </div>

    <div class="submit-button">SUBMIT</div>
    <div class="help-link">HELP</div>
  </div>
</div>
</body>
</html>
```